Business Card Design

Quiet Fernlight - edgy, unique, ontrend clothing for girls 0-12.
I would like simple styling with white background and natural beige/brown font, similar to attached font.

Industry/Entity Type

Clothing

Contact Information for Business Card

Hi, I would like a very simple business card, white background with natural, beige, brown font, Quiet Fernlight. I design and sell clothes for girls 0-12 with a touch of bohemian styling. I would like "Quiet Fernlight" on front and on back -
www.quietfernlight.example.au
Colette Brennick,
0491558213,
colettebrennick@mailvale.example.au

```html
<!DOCTYPE html>
<html lang="en">
<head>
<meta charset="utf-8">
<title>Quiet Fernlight — Business Card</title>
<link rel="stylesheet" href="https://fonts.googleapis.com/css2?family=Delius&display=swap">
<style>
  :root {
    --page-bg: #d9d9d7;
    --card-light: #efe2d1;
    --card-mid: #e4d1bb;
    --card-edge: #d6bfa6;
    --ink: #a3957a;
    --ink-soft: #b3a486;
    --ornament: #cfbc9c;
  }
  * { box-sizing: border-box; margin: 0; padding: 0; }
  html, body {
    width: 1200px;
    height: 1200px;
    overflow: hidden;
    background: var(--page-bg);
  }
  .sheet {
    position: relative;
    width: 1200px;
    height: 1200px;
    display: flex;
    flex-direction: column;
    align-items: center;
    justify-content: center;
    gap: 70px;
  }
  .card {
    position: relative;
    width: 720px;
    height: 440px;
    background: radial-gradient(ellipse at 50% 40%, var(--card-light) 0%, var(--card-mid) 70%, var(--card-edge) 100%);
    box-shadow: 0 6px 18px rgba(0,0,0,0.12);
    font-family: "Delius", cursive;
    color: var(--ink);
  }
  .card-front .ornament {
    position: absolute;
    left: 50%;
    top: 48px;
    width: 270px;
    height: 220px;
    transform: translateX(-50%);
    border-radius: 50%;
    background: radial-gradient(ellipse at center, var(--ornament) 0%, rgba(207,188,156,0.35) 60%, rgba(207,188,156,0) 100%);
  }
  .brand-name {
    position: absolute;
    left: 0;
    right: 0;
    text-align: center;
    font-size: 72px;
    font-weight: 400;
    letter-spacing: 2px;
    color: var(--ink);
  }
  .card-front .brand-name { top: 280px; }
  .card-back .brand-name { top: 300px; }
  .contact {
    position: absolute;
    top: 44px;
    left: 0;
    right: 0;
    text-align: center;
  }
  .contact-name {
    font-size: 46px;
    letter-spacing: 3px;
    margin-bottom: 26px;
  }
  .contact-line {
    font-size: 22px;
    line-height: 38px;
    color: var(--ink-soft);
    letter-spacing: 1px;
  }
</style>
</head>
<body>
  <main class="sheet">
    <section class="card card-front">
      <div class="ornament" role="img" aria-label="Botanical ornament of a fern leaf with small blossoms"></div>
      <p class="brand-name">Quiet Fernlight</p>
    </section>
    <section class="card card-back">
      <div class="contact">
        <p class="contact-name">Colette Brennick</p>
        <p class="contact-line">www.quietfernlight.example.au</p>
        <p class="contact-line">0491558213</p>
        <p class="contact-line">colettebrennick@mailvale.example.au</p>
      </div>
      <p class="brand-name">Quiet Fernlight</p>
    </section>
  </main>
</body>
</html>
```